Sports Therapy and Personal Training

I need a business card design for a new business based in Toronto called "Holbrin Athletics" I am a sports therapist as well as a strength and conditioning coach, therefore I work mainly with high level athletes and physically active people. I am starting my own therapy/training business. The services I will be offering include fitness consultation, personal training, athlete assessments, and rehabilitation therapy. These services will be delivered in peoples homes and/or a facility in which I rent space.

The final design should communicate "high-end" and "quality"

Target Market(s)

athletes and physically active people

Industry/Entity Type

Fitness

Requirements
Must have
• 1. The business logo - files attached

2. my name and credentials

Derek Falloway - CAT(C), CK, CSCS,

Certified Athletic Therapist
Strength and Conditioning Specialist

3. website - www.holbrinathletics.example

4. email address - derek@holbrinathletics.example

5. phone number

```html
<!DOCTYPE html>
<html lang="en">
<head>
<meta charset="utf-8">
<title>Holbrin Athletics – Business Cards</title>
<link rel="stylesheet" href="https://fonts.googleapis.com/css2?family=Mulish:wght@400;600;700;800&display=swap">
<style>
  :root {
    --backdrop: #b8b8b8;
    --card-light: #ffffff;
    --card-edge: #e6e6e6;
    --slate: #6d7283;
    --red: #d41a1f;
    --ink: #2f2f2f;
    --ink-soft: #555555;
    --muted: #8a8a8a;
    --mark: #4a4a4a;
  }
  * { box-sizing: border-box; margin: 0; padding: 0; }
  html, body { width: 1200px; height: 702px; overflow: hidden; }
  body {
    background: var(--backdrop);
    font-family: "Mulish", "Century Gothic", sans-serif;
    position: relative;
  }
  .card {
    position: absolute;
    width: 548px;
    height: 311px;
    border-radius: 16px;
    background: radial-gradient(ellipse at 50% 40%, var(--card-light) 55%, var(--card-edge) 100%);
    box-shadow: 0 2px 6px rgba(0,0,0,.25);
    overflow: hidden;
  }
  .card--tl { left: 35px;  top: 32px; }
  .card--tr { left: 615px; top: 32px; }
  .card--bl { left: 35px;  top: 358px; }
  .card--br { left: 615px; top: 358px; }

  .bar {
    position: absolute;
    top: 22px;
    bottom: 22px;
    width: 12px;
    border-radius: 2px;
  }
  .bar--left { left: 4px; }
  .bar--right { right: 4px; }
  .bar--slate { background: var(--slate); }
  .bar--red { background: var(--red); }

  /* Front */
  .front {
    position: absolute;
    inset: 0;
    display: flex;
    flex-direction: column;
    align-items: center;
    justify-content: flex-end;
    padding-bottom: 28px;
  }
  .front .brand-dot {
    width: 150px; height: 150px;
    border-radius: 50%;
    background: var(--mark);
    margin-bottom: 34px;
  }
  .front .brand-name {
    font-size: 25px;
    font-weight: 800;
    color: var(--ink);
    letter-spacing: .5px;
    text-transform: uppercase;
  }
  .front .tagline {
    margin-top: 3px;
    font-size: 10.5px;
    font-weight: 700;
    color: var(--muted);
    letter-spacing: 1px;
    text-transform: uppercase;
  }

  /* Back */
  .back-brand {
    position: absolute;
    left: 0; right: 0; top: 48px;
    display: flex;
    flex-direction: column;
    align-items: center;
  }
  .back-brand .brand-dot {
    width: 66px; height: 66px;
    border-radius: 50%;
    background: var(--mark);
    margin-bottom: 12px;
  }
  .back-brand .brand-name {
    font-size: 11px;
    font-weight: 800;
    color: var(--ink);
    text-transform: uppercase;
    letter-spacing: .3px;
  }
  .back-brand .tagline {
    font-size: 5px;
    font-weight: 700;
    color: var(--muted);
    letter-spacing: .5px;
    text-transform: uppercase;
  }
  .person {
    position: absolute;
    left: 59px;
    top: 198px;
  }
  .person .name {
    font-size: 20px;
    font-weight: 800;
    color: var(--red);
    text-transform: uppercase;
    line-height: 1;
  }
  .person .credentials {
    text-align: right;
    font-size: 9px;
    font-weight: 700;
    color: var(--ink-soft);
    margin-top: 1px;
  }
  .person .roles {
    list-style: none;
    margin-top: 8px;
    font-size: 7px;
    font-weight: 700;
    color: var(--ink-soft);
    text-transform: uppercase;
    line-height: 14px;
  }
  .person .roles li::before { content: "• "; }
  .contact {
    position: absolute;
    left: 287px;
    top: 200px;
    list-style: none;
  }
  .contact li {
    display: flex;
    align-items: center;
    height: 21px;
    font-size: 9.5px;
    font-weight: 700;
    color: var(--ink);
    text-transform: uppercase;
  }
  .contact svg {
    width: 11px; height: 11px;
    margin-right: 10px;
    fill: var(--ink-soft);
  }
</style>
</head>
<body>

<!-- Front, slate -->
<section class="card card--tl">
  <span class="bar bar--left bar--slate"></span>
  <span class="bar bar--right bar--slate"></span>
  <div class="front">
    <span class="brand-dot"></span>
    <p class="brand-name">Holbrin Athletics</p>
    <p class="tagline">Sports Medicine • Strength and Conditioning</p>
  </div>
</section>

<!-- Back, slate -->
<section class="card card--tr">
  <span class="bar bar--left bar--slate"></span>
  <span class="bar bar--right bar--slate"></span>
  <div class="back-brand">
    <span class="brand-dot"></span>
    <p class="brand-name">Holbrin Athletics</p>
    <p class="tagline">Sports Medicine • Strength and Conditioning</p>
  </div>
  <div class="person">
    <p class="name">Derek Falloway</p>
    <p class="credentials">CAT(C), CK, CSCS</p>
    <ul class="roles">
      <li>Certified Athletic Therapist</li>
      <li>Strength and Conditioning Specialist</li>
    </ul>
  </div>
  <ul class="contact">
    <li><svg viewBox="0 0 12 12"><rect x="3" y="0" width="6" height="12" rx="1.2"/></svg>00 0000 0000</li>
    <li><svg viewBox="0 0 12 12"><path d="M0 2h12v8H0z M1 3l5 3.5L11 3" stroke="#fff" stroke-width=".8"/></svg>derek@holbrinathletics.example</li>
    <li><svg viewBox="0 0 12 12"><circle cx="6" cy="6" r="5.5"/><path d="M1 6h10M6 .5c-3 3-3 8 0 11M6 .5c3 3 3 8 0 11" stroke="#fff" stroke-width=".8" fill="none"/></svg>www.holbrinathletics.example</li>
  </ul>
</section>

<!-- Back, red -->
<section class="card card--bl">
  <span class="bar bar--left bar--red"></span>
  <span class="bar bar--right bar--red"></span>
  <div class="back-brand">
    <span class="brand-dot"></span>
    <p class="brand-name">Holbrin Athletics</p>
    <p class="tagline">Sports Medicine • Strength and Conditioning</p>
  </div>
  <div class="person">
    <p class="name">Derek Falloway</p>
    <p class="credentials">CAT(C), CK, CSCS</p>
    <ul class="roles">
      <li>Certified Athletic Therapist</li>
      <li>Strength and Conditioning Specialist</li>
    </ul>
  </div>
  <ul class="contact">
    <li><svg viewBox="0 0 12 12"><rect x="3" y="0" width="6" height="12" rx="1.2"/></svg>00 0000 0000</li>
    <li><svg viewBox="0 0 12 12"><path d="M0 2h12v8H0z M1 3l5 3.5L11 3" stroke="#fff" stroke-width=".8"/></svg>derek@holbrinathletics.example</li>
    <li><svg viewBox="0 0 12 12"><circle cx="6" cy="6" r="5.5"/><path d="M1 6h10M6 .5c-3 3-3 8 0 11M6 .5c3 3 3 8 0 11" stroke="#fff" stroke-width=".8" fill="none"/></svg>www.holbrinathletics.example</li>
  </ul>
</section>

<!-- Front, red -->
<section class="card card--br">
  <span class="bar bar--left bar--red"></span>
  <span class="bar bar--right bar--red"></span>
  <div class="front">
    <span class="brand-dot"></span>
    <p class="brand-name">Holbrin Athletics</p>
    <p class="tagline">Sports Medicine • Strength and Conditioning</p>
  </div>
</section>

</body>
</html>
```